I need a cover designed for a leadership book to fit my brand of my podcast, Chat with Your Druggist, www.remedyguidance-hub.com, with blues and greens and a professional look since it will be for a professional audience of pharmacists.

Some ideas for an image for the cover might be a woman's hand holding a compass with a road, but I welcome other ideas.

Title of the book is
"Where Chemists Steer: Insights from Ladies [in Focus] Who Are Guiding, Thriving, and Shaping Dispensaries"

```html
<!DOCTYPE html>
<html lang="en">
<head>
<meta charset="utf-8">
<title>Where Chemists Steer – Book Cover</title>
<link rel="stylesheet" href="https://fonts.googleapis.com/css2?family=Bebas+Neue&family=Montserrat:ital,wght@0,500;0,600;0,700;1,500&display=swap">
<style>
  :root {
    --backdrop: #3b3b3d;
    --navy: #2b3080;
    --navy-deep: #1f2462;
    --navy-ink: #262c6c;
    --green: #8ee23c;
    --green-deep: #7ccd2f;
    --white: #ffffff;
    --compass-gold: #b08a4a;
    --compass-dark: #5a4424;
    --photo-tone: #d9b8a2;
  }
  * { box-sizing: border-box; margin: 0; padding: 0; }
  html, body { width: 1200px; height: 1200px; overflow: hidden; }
  body {
    background: var(--backdrop);
    font-family: "Montserrat", Arial, sans-serif;
    position: relative;
  }
  .cover-wrap {
    position: absolute;
    left: 50px; top: 210px;
    width: 1100px; height: 780px;
    display: flex;
    box-shadow: 0 20px 40px rgba(0,0,0,.35);
  }
  .panel { position: relative; height: 100%; overflow: hidden; }
  .panel-back, .panel-front { width: 520px; }
  .panel-spine { width: 60px; }

  .band-top {
    position: absolute; left: 0; right: 0; top: 0;
    background: radial-gradient(ellipse at 50% 35%, var(--navy) 0%, var(--navy-deep) 100%);
  }
  .band-bottom {
    position: absolute; left: 0; right: 0; bottom: 0;
    background: linear-gradient(180deg, var(--green) 0%, var(--green-deep) 100%);
  }
  .panel-front .band-top, .panel-spine .band-top { height: 500px; }
  .panel-front .band-bottom, .panel-spine .band-bottom { top: 500px; }
  .panel-back .band-top { height: 520px; }
  .panel-back .band-bottom { top: 520px; }

  /* Front */
  .front-title {
    position: absolute; left: 50px; top: 50px; right: 30px;
    font-family: "Bebas Neue", Impact, sans-serif;
    line-height: .88;
  }
  .front-title .title-small { display: block; color: var(--green); font-size: 76px; }
  .front-title .title-large { display: block; color: var(--white); font-size: 236px; margin-left: -6px; line-height: .86; }
  .compass {
    position: absolute; left: 205px; top: 420px;
    width: 110px; height: 110px; border-radius: 50%;
    background: radial-gradient(circle at 45% 40%, #e9dcbc 0%, #c9a96a 40%, var(--compass-gold) 60%, var(--compass-dark) 100%);
    box-shadow: 0 4px 10px rgba(0,0,0,.4);
  }
  .front-subtitle {
    position: absolute; left: 30px; right: 30px; top: 545px;
    text-align: center; color: var(--navy-ink);
    font-weight: 600; font-size: 19px; line-height: 1.3;
  }
  .front-author {
    position: absolute; left: 0; right: 0; top: 690px;
    text-align: center; color: var(--navy-ink);
    font-family: "Bebas Neue", Impact, sans-serif; font-size: 42px; letter-spacing: 1px;
  }

  /* Spine */
  .spine-text {
    position: absolute; left: 0; width: 60px;
    writing-mode: vertical-rl;
    font-family: "Bebas Neue", Impact, sans-serif;
    display: flex; align-items: center;
    letter-spacing: 3px;
  }
  .spine-title { top: 30px; height: 440px; color: var(--green); font-size: 26px; }
  .spine-title .white { color: var(--white); margin-top: 8px; }
  .spine-author { top: 525px; height: 240px; color: var(--navy-ink); font-size: 24px; }

  /* Back */
  .back-heading {
    position: absolute; top: 40px; left: 0; right: 0; text-align: center;
    font-family: "Bebas Neue", Impact, sans-serif; font-size: 40px; color: var(--green); letter-spacing: 1px;
  }
  .back-heading .white { color: var(--white); }
  .back-tagline {
    position: absolute; top: 110px; left: 40px; right: 40px; text-align: center;
    color: var(--white); font-weight: 700; font-size: 15px; line-height: 1.35; text-transform: uppercase;
  }
  .endorsement {
    position: absolute; left: 40px; right: 40px;
    color: var(--white); font-size: 12.5px; line-height: 1.45; text-align: center;
  }
  .endorsement-one { top: 200px; }
  .endorsement-two { top: 370px; }
  .endorsement cite {
    display: block; margin-top: 6px; color: var(--green); font-style: italic; font-weight: 500;
  }
  .author-photo {
    position: absolute; left: 20px; top: 545px; width: 96px; height: 100px;
    background: linear-gradient(160deg, #f2ece6 0%, var(--photo-tone) 60%, #b23b36 100%);
    border: 3px solid var(--white);
  }
  .back-author {
    position: absolute; left: 130px; top: 545px;
    font-family: "Bebas Neue", Impact, sans-serif; font-size: 34px; color: var(--navy-ink);
  }
  .back-bio {
    position: absolute; left: 130px; right: 30px; top: 590px;
    font-size: 12.5px; line-height: 1.45; color: var(--navy-ink); text-align: justify;
  }
</style>
</head>
<body>
  <div class="cover-wrap">
    <section class="panel panel-back">
      <div class="band-top"></div>
      <div class="band-bottom"></div>
      <h2 class="back-heading">Where Chemists <span class="white">Steer</span></h2>
      <p class="back-tagline">Be inspired along your leadership journey by women in pharmacy who are leading, succeeding, and making an impact.</p>
      <blockquote class="endorsement endorsement-one">
        “I was first introduced to Marlowe’s work a few years ago through her podcast Chat with Your Druggist and meet her personally for a Mastermind weekend in Savannah. She has always been passionate about female leadership and empowering women in pharmacy. I was so inspired by the stories of the women featured in the book and I look forward to our bright future as leaders!”
        <cite>- Renata Colby, PharmD</cite>
      </blockquote>
      <blockquote class="endorsement endorsement-two">
        “Marlowe’s book explores the possibilities allowing women pharmacist’s to dream big, becoming leaders, entrepreneurs, social networkers, clinicians and the best health care providers they can be. These women do not sit by waiting for opportunities to come, they create and plan their successes in a variety of career paths”
        <cite>- Dana Whitfield, PharmD</cite>
      </blockquote>
      <div class="author-photo" role="img" aria-label="Portrait photograph of the author in a white coat"></div>
      <h3 class="back-author">Marlowe Hastings, PharmD, MBA</h3>
      <p class="back-bio">Dr. Marlowe Hastings is a clinically and business trained pharmacist who’s been practicing for the past decade in a variety of healthcare settings. Dr. Hastings is the creator and host of the Chat with Your Druggist podcast, with over 160 episodes sharing stories of successful pharmacy leaders and healthcare trends. She is passionate about inspiring future leaders and promoting the pharmacy profession.</p>
    </section>

    <section class="panel panel-spine">
      <div class="band-top"></div>
      <div class="band-bottom"></div>
      <div class="spine-text spine-title">Where Chemists <span class="white">Steer</span></div>
      <div class="spine-text spine-author">Marlowe Hastings</div>
    </section>

    <section class="panel panel-front">
      <div class="band-top"></div>
      <div class="band-bottom"></div>
      <h1 class="front-title">
        <span class="title-small">Where</span>
        <span class="title-small">Chemists</span>
        <span class="title-large">Steer</span>
      </h1>
      <div class="compass" role="img" aria-label="Brass navigation compass"></div>
      <p class="front-subtitle">Insights from Ladies [in Focus] Who Are Guiding, Thriving, and Shaping Dispensaries</p>
      <p class="front-author">Marlowe Hastings, PharmD, MBA</p>
    </section>
  </div>
</body>
</html>
```